Business Cards Needed For Veterinary Business

Looking for a business card design for a veterinary blood bank. We would like it to be clean and professional on appearance but still warm and inviting. We would like to utilize our logo and similar coloring. We will use our phone number, email, website, employee name, employee title.

We do not want a bunch of animated animal photos but do not need the style to be as clinical as a laboratory or human medical procedure office.

We are looking for some creative ideas to choose from so that we can generate a standout professional business card for our management team to utilize.

Target Market(s)

professionals

Industry/Entity Type

veterinary

Contact Information for Business Card

employee name, employee title, phone number, website URL, email

Font styles to use
Sans Serif

Colors
0054AA
0677BA
7BADD7
CADEEF
E8F1F8
EB3D1F
EC4F4E
F09395
F8D3D4
FCEDEE

Requirements
Nice to have
• creative design
Should not have
• animated photos

```html
<!DOCTYPE html>
<html lang="en">
<head>
<meta charset="utf-8">
<title>Kestrel Veterinary Blood Bank – Business Card</title>
<link rel="stylesheet" href="https://fonts.googleapis.com/css2?family=Arimo:wght@700&family=Lato:wght@400&family=Montserrat:wght@700&display=swap">
<style>
  :root {
    --brand-blue: #2459d8;
    --brand-red: #ee2a1d;
    --slate: #6b7478;
    --ink: #1d1d1f;
    --paper: #ffffff;
    --page: #ffffff;
  }
  * { margin: 0; padding: 0; box-sizing: border-box; }
  html, body { width: 915px; height: 1200px; overflow: hidden; background: var(--page); }
  .sheet { position: relative; width: 915px; height: 1200px; }

  .card {
    position: absolute; left: 74px; width: 765px; height: 438px;
    background: var(--paper); overflow: hidden;
    box-shadow: 10px 14px 26px rgba(0,0,0,0.35);
  }
  .card--front { top: 127px; }
  .card--back  { top: 632px; }

  /* brand lockup */
  .brand { position: absolute; display: flex; align-items: center; gap: 16px; }
  .brand__dot { width: 86px; height: 86px; border-radius: 50%; background: var(--brand-red); flex: none; }
  .brand__name {
    font-family: "Montserrat", sans-serif; font-weight: 700; color: var(--brand-red);
    line-height: 1; text-transform: uppercase;
  }
  .brand__name .line-main { display: block; font-size: 52px; letter-spacing: 1px; }
  .brand__name .line-sub  { display: block; font-size: 17.5px; margin-top: 8px; letter-spacing: 0.3px; }
  .card--front .brand { right: 38px; top: 36px; }
  .card--back .brand { left: 164px; top: 128px; }
  .card--back .brand__dot { width: 104px; height: 104px; }
  .card--back .brand__name .line-main { font-size: 60px; }
  .card--back .brand__name .line-sub  { font-size: 20px; }

  /* person */
  .person { position: absolute; left: 32px; top: 170px; }
  .person__name {
    font-family: "Arimo", sans-serif; font-weight: 700; font-size: 40px;
    color: var(--brand-blue); letter-spacing: 0.5px; line-height: 1;
  }
  .person__title {
    font-family: "Arimo", sans-serif; font-weight: 700; font-size: 16.5px;
    color: var(--slate); margin-top: 9px; letter-spacing: 0.3px;
  }

  .contact { position: absolute; left: 32px; top: 264px; list-style: none; }
  .contact__item {
    display: flex; align-items: center; gap: 10px; height: 26.5px;
    font-family: "Lato", sans-serif; font-size: 18px; color: var(--ink);
  }
  .contact__icon { width: 20px; height: 18px; flex: none; }

  .address {
    position: absolute; right: 38px; top: 296px; text-align: right;
    font-family: "Lato", sans-serif; font-size: 18px; color: var(--ink); line-height: 24px;
    font-style: normal;
  }

  .wave, .stripes { position: absolute; left: 0; bottom: 0; width: 765px; }
</style>
</head>
<body>
<main class="sheet">

  <section class="card card--front" aria-label="Card front">
    <div class="brand">
      <span class="brand__dot" aria-hidden="true"></span>
      <p class="brand__name"><span class="line-main">Kestrel</span><span class="line-sub">Veterinary Blood Bank</span></p>
    </div>

    <div class="person">
      <h1 class="person__name">MARLO TESSING</h1>
      <p class="person__title">DIRECTOR</p>
    </div>

    <ul class="contact">
      <li class="contact__item">
        <svg class="contact__icon" viewBox="0 0 20 18" aria-hidden="true">
          <path d="M4 2c1-.6 2 .2 2.6 1.4l1 2c.3.7 0 1.3-.6 1.7l-.8.5c.8 1.9 2.3 3.4 4.2 4.2l.5-.8c.4-.6 1-.9 1.7-.6l2 1c1.2.6 2 1.6 1.4 2.6-.8 1.5-2.4 2.3-4 1.8C7.6 14.5 3.5 10.4 2.2 6 1.7 4.4 2.5 2.8 4 2z" fill="var(--brand-blue)"/>
        </svg>
        301-555-0148
      </li>
      <li class="contact__item">
        <svg class="contact__icon" viewBox="0 0 20 18" aria-hidden="true">
          <rect x="1" y="3" width="18" height="12" fill="var(--brand-blue)"/>
          <path d="M1.5 3.5 10 10l8.5-6.5" fill="none" stroke="#fff" stroke-width="1.4"/>
        </svg>
        marlo@mailbox.example
      </li>
      <li class="contact__item">
        <svg class="contact__icon" viewBox="0 0 20 18" aria-hidden="true">
          <circle cx="10" cy="9" r="8" fill="var(--brand-blue)"/>
          <path d="M2 9h16M10 1c-3 3-3 13 0 16M10 1c3 3 3 13 0 16" fill="none" stroke="#fff" stroke-width="1.2"/>
        </svg>
        www.kestrelvetbank.com
      </li>
    </ul>

    <address class="address">2275 Linden Ct #118<br>Fairview, MD 20999</address>

    <svg class="wave" viewBox="0 0 765 90" height="90" aria-hidden="true">
      <path d="M0 26 C 120 -6, 300 10, 470 50 C 600 78, 690 44, 765 30 L765 90 L0 90 Z" fill="var(--brand-red)"/>
      <path d="M0 34 C 120 4, 300 18, 470 56 C 600 82, 690 50, 765 36 L765 90 L0 90 Z" fill="var(--paper)"/>
      <path d="M0 40 C 130 14, 300 30, 470 62 C 600 84, 690 58, 765 42 L765 90 L0 90 Z" fill="var(--brand-blue)"/>
    </svg>
  </section>

  <section class="card card--back" aria-label="Card back">
    <div class="brand">
      <span class="brand__dot" aria-hidden="true"></span>
      <p class="brand__name"><span class="line-main">Kestrel</span><span class="line-sub">Veterinary Blood Bank</span></p>
    </div>

    <svg class="stripes" viewBox="0 0 765 88" height="88" aria-hidden="true">
      <rect x="0" y="0" width="765" height="13" fill="var(--brand-blue)"/>
      <rect x="0" y="21" width="765" height="13" fill="var(--slate)"/>
      <rect x="0" y="42" width="765" height="46" fill="var(--brand-red)"/>
    </svg>
  </section>

</main>
</body>
</html>
```